Wordpress template re-design of current website

We need a WordPress template design and new look for our existing website. Our existing site it located at www.velquor.com.au We are a tech company and want a fresh, clean modern website that matches our brand, services and logo colors. Our main Services are hospitality solutions, Velquor TV solution and managed networks, more information on these can come from our existing website.

Target Market(s)

We are a tech company so must have a modern feel for new technology

Industry/Entity Type

It Company

Number of Pages Required

5+ page

Font styles to use
Sans Serif

Requirements
Must have
• Be based on a wordpress templete design and match the services that we have in our existing website, in the testimonials want a place for video testimonials as well as text. Nice clean icons used for graphics to represent services.
Nice to have
• nice visual representation of our services in the way of clean icons etc
Should not have
• Clutter

```html
<!DOCTYPE html>
<html lang="en">
<head>
<meta charset="utf-8">
<title>Velquor — Blog</title>
<link href="https://fonts.googleapis.com/css2?family=Roboto:wght@400;500;700&display=swap" rel="stylesheet">
<style>
:root{
  --navy:#123f80;
  --title:#24508a;
  --slate:#6c7d89;
  --slate-dark:#5d6d78;
  --text:#555b60;
  --muted:#8a9096;
  --rule:#e3e5e7;
  --light:#eceef0;
  --white:#ffffff;
  --link:#2b5ea8;
}
*{box-sizing:border-box;margin:0;padding:0}
html,body{width:1200px;height:3333px;overflow:hidden}
body{position:relative;background:var(--white);font-family:'Roboto',sans-serif;color:var(--text)}
.abs{position:absolute}

/* header */
.brand{left:73px;top:30px;display:flex;align-items:center;gap:12px}
.brand-name{font-size:40px;font-weight:700;color:var(--navy);letter-spacing:-.5px}
.brand-dot{width:22px;height:22px;border-radius:50%;background:var(--navy)}
.phone{left:838px;top:42px;display:flex;align-items:center;gap:10px;font-size:19px;color:#4a5056}
.portal{left:1004px;top:38px;width:122px;height:38px;border-radius:19px;background:var(--navy);color:var(--white);font-size:14px;font-weight:700;display:flex;align-items:center;justify-content:center;letter-spacing:.5px}

.nav{left:0;top:115px;width:1200px;height:50px;background:var(--slate)}
.nav a{position:absolute;top:16px;color:var(--white);font-size:14px;font-weight:700;text-decoration:none;letter-spacing:.3px}
.search{position:absolute;left:862px;top:10px;width:264px;height:30px;border-radius:15px;background:var(--white);display:flex;align-items:center;padding-left:14px;gap:10px;font-size:12px;color:#a0a5aa}

.hero{left:0;top:165px;width:1200px;height:230px;background:linear-gradient(100deg,#8b7560 0%,#b9a48c 30%,#6f6760 60%,#c9c4be 100%)}
.hero h1{position:absolute;left:73px;top:100px;color:var(--white);font-size:28px;font-weight:700;letter-spacing:.3px}

/* posts */
.post{left:73px;width:694px}
.post h2{font-size:22px;font-weight:500;color:var(--title)}
.meta{margin-top:12px;display:flex;gap:22px;font-size:11px;color:var(--muted);align-items:center}
.meta span{display:flex;align-items:center;gap:7px}
.meta i{display:inline-block;width:12px;height:11px;background:#b5babe;border-radius:2px}
.post-photo{margin-top:23px;width:694px;height:362px}
.excerpt{margin-top:32px;font-size:13px;line-height:22px;color:var(--text)}
.excerpt a{color:var(--link);text-decoration:none}
.share{margin-top:35px;border-top:1px solid var(--rule);border-bottom:1px solid var(--rule);height:33px;display:flex;justify-content:flex-end;align-items:center;gap:8px}
.btn-s{display:flex;align-items:center;gap:4px;height:18px;padding:0 5px;border:1px solid #c8ccd0;border-radius:3px;font-size:10px;color:#3d4a58;background:#f5f6f7}
.btn-s b{width:9px;height:9px;border-radius:2px;background:#6a7f9a}
.count{font-size:10px;color:#666;border:1px solid #d5d8db;padding:1px 5px;border-radius:2px}

/* sidebar */
.side-h{font-size:21px;font-weight:500;color:#3e4a55;text-transform:uppercase}
.tabs{left:793px;top:478px;width:334px;height:35px;border-bottom:3px solid var(--navy);display:flex}
.tabs span{height:32px;display:flex;align-items:center;justify-content:center;font-size:14px;color:#555;background:var(--light);border-right:1px solid #d8dadd}
.tabs .on{background:var(--navy);color:var(--white)}
.pop{left:793px;width:334px;height:102px;border-bottom:1px solid var(--rule);display:flex;gap:20px;padding-top:12px}
.pop .thumb{width:107px;height:68px;flex:none}
.pop p{font-size:13px;line-height:19px;color:var(--link)}
.tags{left:793px;top:1094px;width:334px;display:flex;flex-wrap:wrap;gap:9px 10px}
.tag{height:22px;padding:0 16px;background:var(--light);border-radius:11px;font-size:10px;color:#9aa0a5;display:flex;align-items:center}
.arch{left:793px;top:1292px;font-size:13px;color:#4a5560}
.arch li{list-style:none;height:24px;display:flex;align-items:center;gap:8px}
.arch .m{padding-left:28px;color:#6d747a}
.arch .yr b{width:11px;height:11px;border-radius:50%;border:2px solid #3f4a55;display:inline-block}
.arch .open b{border-color:var(--navy)}
.arch .open{color:var(--navy)}

/* pagination */
.pager{left:323px;top:2958px;display:flex}
.pager span{height:30px;min-width:30px;padding:0 10px;border:1px solid #d4d7da;margin-left:-1px;font-size:13px;color:#555;display:flex;align-items:center;justify-content:center}
.pager .cur{background:#e4e6e8}

/* footer */
.footer{left:0;top:3038px;width:1200px;height:257px;background:var(--slate)}
.f-col{position:absolute;top:47px;color:var(--white)}
.f-col h4{font-size:14px;font-weight:700;margin-bottom:12px;letter-spacing:.2px}
.f-col li{list-style:none;font-size:12px;line-height:24px}
.f-row{display:flex;gap:14px;font-size:12px;line-height:18px;margin-bottom:12px}
.f-row i{width:12px;height:14px;flex:none;margin-top:2px}
.news p{font-size:12px;line-height:20px;width:330px}
.field{position:absolute;width:311px;height:36px;background:var(--white);border-radius:4px;display:flex;align-items:center;gap:10px;padding-left:12px;font-size:12px;color:#9aa0a5}
.field b{width:14px;height:14px;border-radius:50%;background:#9aa4ac}
.signup{position:absolute;left:1024px;top:135px;width:103px;height:80px;background:#8b9ba6;border-radius:4px;display:flex;flex-direction:column;align-items:center;justify-content:center;gap:8px;color:var(--white);font-size:15px;font-weight:700}
.bottom{left:0;top:3295px;width:1200px;height:38px;background:#e9ebec}
.copy{position:absolute;left:73px;top:12px;font-size:12px;color:#6b7278;display:flex;gap:10px;align-items:center}
.copy b{width:10px;height:10px;border-radius:50%;background:#8b949b}
.chat{position:absolute;left:911px;top:7px;width:216px;height:31px;background:#5f6f7a;border-radius:5px 5px 0 0;color:var(--white);font-size:12px;display:flex;align-items:center;padding:0 12px;gap:10px}
.chat .sp{flex:1}
.chat i{width:12px;height:12px;border-radius:50%;background:#c7ced3}
</style>
</head>
<body>

<header>
  <div class="abs brand"><span class="brand-name">Velquor</span><span class="brand-dot"></span></div>
  <div class="abs phone">
    <svg width="22" height="22" viewBox="0 0 22 22"><circle cx="11" cy="11" r="11" fill="#123f80"/><path d="M8 6c1 0 1.5 2 1.5 2.5S8.5 9.5 8.8 10.3s2 2.7 2.9 2.9 1.3-.7 1.8-.7 2.5.5 2.5 1.5-1.2 2-2.5 2C10 16 6 12 6 8.5 6 7 7 6 8 6z" fill="#fff"/></svg>
    1300 555 014
  </div>
  <div class="abs portal">PORTAL</div>
</header>

<nav class="abs nav">
  <a style="left:111px">HOME</a>
  <a style="left:229px">SERVICES</a>
  <a style="left:374px">ABOUT</a>
  <a style="left:500px">OUR WORK</a>
  <a style="left:653px">CONTACT</a>
  <div class="search">
    <svg width="12" height="12" viewBox="0 0 12 12"><circle cx="5" cy="5" r="3.8" fill="none" stroke="#8a9096" stroke-width="1.5"/><path d="M8 8l3 3" stroke="#8a9096" stroke-width="1.5"/></svg>Search
  </div>
</nav>

<section class="abs hero" role="img" aria-label="Photo of hands typing on a laptop keyboard">
  <h1>OUR LATEST BLOG POSTS</h1>
</section>

<!-- posts -->
<article class="abs post" style="top:432px">
  <h2>Lorem ipsum dolor sit amet in futurum</h2>
  <div class="meta"><span><i></i>Posted By Sam Porter</span><span><i></i>13 Jul 2015</span><span><i></i>(0) Comments</span></div>
  <div class="post-photo" role="img" aria-label="Photo of a group of friends looking at a tablet in a café" style="background:linear-gradient(120deg,#d9d2c4,#8a6d5a 45%,#5f4a44 70%,#b8ab9c)"></div>
  <p class="excerpt">Lorem ipsum dolor sit amet, consectetuer adipiscing elit, sed diam nonummy nibh euismod tincidunt ut laoreet dolore magna aliquam erat volutpat. Ut wisi enim ad minim veniam, quis nostrud exerci tation ullamcorper suscipit lobortis nisl ut aliquip ex ea commodo consequat. <a>[Readmore...]</a></p>
  <div class="share"><span class="btn-s"><b></b>Like</span><span class="count">1.5k</span><span class="btn-s"><b></b>Tweet</span><span class="count">806</span><span class="btn-s"><b></b>+1</span><span class="count">853</span><span class="btn-s"><b></b>Share</span><span class="count">142</span><span class="btn-s"><b></b>Pin it</span><span class="count">+3</span></div>
</article>

<article class="abs post" style="top:1061px">
  <h2>Lorem ipsum dolor sit amet in futurum</h2>
  <div class="meta"><span><i></i>Posted By Sam Porter</span><span><i></i>13 Jul 2015</span><span><i></i>(0) Comments</span></div>
  <div class="post-photo" role="img" aria-label="Photo of four young people outdoors with coffee cups and a tablet" style="background:linear-gradient(120deg,#8fa26a,#4d4640 40%,#7b5f52 65%,#c8b89e)"></div>
  <p class="excerpt">Lorem ipsum dolor sit amet, consectetuer adipiscing elit, sed diam nonummy nibh euismod tincidunt ut laoreet dolore magna aliquam erat volutpat. Ut wisi enim ad minim veniam, quis nostrud exerci tation ullamcorper suscipit lobortis nisl ut aliquip ex ea commodo consequat. <a>[Readmore...]</a></p>
  <div class="share"><span class="btn-s"><b></b>Like</span><span class="count">1.5k</span><span class="btn-s"><b></b>Tweet</span><span class="count">806</span><span class="btn-s"><b></b>+1</span><span class="count">853</span><span class="btn-s"><b></b>Share</span><span class="count">142</span><span class="btn-s"><b></b>Pin it</span><span class="count">+3</span></div>
</article>

<article class="abs post" style="top:1690px">
  <h2>Lorem ipsum dolor sit amet in futurum</h2>
  <div class="meta"><span><i></i>Posted By Sam Porter</span><span><i></i>13 Jul 2015</span><span><i></i>(0) Comments</span></div>
  <div class="post-photo" role="img" aria-label="Photo of three friends laughing over drinks and a tablet" style="background:linear-gradient(120deg,#e6c98f,#c59a6c 35%,#7d6a78 65%,#a59c90)"></div>
  <p class="excerpt">Lorem ipsum dolor sit amet, consectetuer adipiscing elit, sed diam nonummy nibh euismod tincidunt ut laoreet dolore magna aliquam erat volutpat. Ut wisi enim ad minim veniam, quis nostrud exerci tation ullamcorper suscipit lobortis nisl ut aliquip ex ea commodo consequat. <a>[Readmore...]</a></p>
  <div class="share"><span class="btn-s"><b></b>Like</span><span class="count">1.5k</span><span class="btn-s"><b></b>Tweet</span><span class="count">806</span><span class="btn-s"><b></b>+1</span><span class="count">853</span><span class="btn-s"><b></b>Share</span><span class="count">142</span><span class="btn-s"><b></b>Pin it</span><span class="count">+3</span></div>
</article>

<article class="abs post" style="top:2319px">
  <h2>Lorem ipsum dolor sit amet in futurum</h2>
  <div class="meta"><span><i></i>Posted By Sam Porter</span><span><i></i>13 Jul 2015</span><span><i></i>(0) Comments</span></div>
  <div class="post-photo" role="img" aria-label="Photo of a group of young professionals standing together in an office" style="background:linear-gradient(120deg,#d8d4cc,#6d7486 40%,#a4877a 65%,#e2dfd9)"></div>
  <p class="excerpt">Lorem ipsum dolor sit amet, consectetuer adipiscing elit, sed diam nonummy nibh euismod tincidunt ut laoreet dolore magna aliquam erat volutpat. Ut wisi enim ad minim veniam, quis nostrud exerci tation ullamcorper suscipit lobortis nisl ut aliquip ex ea commodo consequat. <a>[Readmore...]</a></p>
  <div class="share"><span class="btn-s"><b></b>Like</span><span class="count">1.5k</span><span class="btn-s"><b></b>Tweet</span><span class="count">806</span><span class="btn-s"><b></b>+1</span><span class="count">853</span><span class="btn-s"><b></b>Share</span><span class="count">142</span><span class="btn-s"><b></b>Pin it</span><span class="count">+3</span></div>
</article>

<!-- sidebar -->
<h3 class="abs side-h" style="left:793px;top:428px">Most Popular</h3>
<div class="abs tabs"><span class="on" style="width:84px">Popular</span><span style="width:86px">Comments</span><span style="width:115px">Reccomanded</span></div>

<div class="abs pop" style="top:516px"><div class="thumb" role="img" aria-label="Thumbnail of people working at laptops" style="background:#6b7a8c"></div><p>Lorem ipsum dolor sit amet, euismod tincidunt ut laoreet aliquam erat volutpat.</p></div>
<div class="abs pop" style="top:618px"><div class="thumb" role="img" aria-label="Thumbnail of colleagues in a meeting" style="background:#a9b2ba"></div><p>Lorem ipsum dolor sit amet, euismod tincidunt ut laoreet aliquam erat volutpat.</p></div>
<div class="abs pop" style="top:720px"><div class="thumb" role="img" aria-label="Thumbnail of a team at a desk" style="background:#7d6f66"></div><p>Lorem ipsum dolor sit amet, euismod tincidunt ut laoreet aliquam erat volutpat.</p></div>
<div class="abs pop" style="top:822px"><div class="thumb" role="img" aria-label="Thumbnail of business people shaking hands" style="background:#8aa0b5"></div><p>Lorem ipsum dolor sit amet, euismod tincidunt ut laoreet aliquam erat volutpat.</p></div>
<div class="abs pop" style="top:924px"><div class="thumb" role="img" aria-label="Thumbnail of a presentation in an office" style="background:#4f6078"></div><p>Lorem ipsum dolor sit amet, euismod tincidunt ut laoreet aliquam erat volutpat.</p></div>

<h3 class="abs side-h" style="left:793px;top:1041px">Popular Tags</h3>
<div class="abs tags">
  <span class="tag">Lorem ipsum</span><span class="tag">Lorem sit</span><span class="tag">Lorem</span><span class="tag">Fixed</span>
  <span class="tag">Lorem ipsum dolor sit</span><span class="tag">Lorem dolor</span><span class="tag">Generators</span>
  <span class="tag">Lorem ipsum</span><span class="tag">Lorem dolor</span><span class="tag">Generators</span>
  <span class="tag">Lorem ipsum dolor sit</span><span class="tag">Shopping</span><span class="tag">Fixed</span>
</div>

<h3 class="abs side-h" style="left:793px;top:1243px">Blog Archives</h3>
<ul class="abs arch">
  <li class="yr open"><b></b>2015 (14)</li>
  <li class="m">December (1)</li>
  <li class="m">November (1)</li>
  <li class="m">October (2)</li>
  <li class="m">September (1)</li>
  <li class="m">August (2)</li>
  <li class="m">July (5)</li>
  <li class="m">June (2)</li>
  <li style="height:16px"></li>
  <li class="yr"><b></b>2014 (9)</li>
  <li class="yr"><b></b>2013 (15)</li>
  <li class="yr"><b></b>2012 (9)</li>
  <li class="yr"><b></b>2015 (10)</li>
</ul>

<div class="abs pager"><span>Prev</span><span class="cur">1</span><span>2</span><span>3</span><span>Next</span></div>

<footer class="abs footer">
  <div class="f-col" style="left:73px"><h4>QUICK LINKS</h4><ul><li>Home</li><li>Services</li><li>About</li><li>Our Work</li><li>Contact</li></ul></div>
  <div class="f-col" style="left:253px"><h4>USEFUL LINKS</h4><ul><li>Case Studies</li><li>Testimonials</li><li>News</li><li>Resellers</li></ul></div>
  <div class="f-col" style="left:467px"><h4>CONTACT US</h4>
    <div class="f-row"><i><svg width="12" height="14" viewBox="0 0 12 14"><path d="M6 0a5 5 0 0 1 5 5c0 4-5 9-5 9S1 9 1 5a5 5 0 0 1 5-5z" fill="#c7ced3"/><circle cx="6" cy="5" r="2" fill="#6c7d89"/></svg></i><span>48 Harbour Lane<br>Lakeside, QLD 4000</span></div>
    <div class="f-row"><i><svg width="12" height="14" viewBox="0 0 12 14"><path d="M3 1c1 0 1.5 2 1.5 2.5S3.5 4.5 3.8 5.5s2 3 3 3.3 1.2-.8 1.7-.8S11 8.5 11 9.5 10 12 9 12C5 12 1 7 1 3.5 1 2 2 1 3 1z" fill="#c7ced3"/></svg></i><span>1300 555 014</span></div>
    <div class="f-row"><i><svg width="12" height="14" viewBox="0 0 12 14"><rect x="0" y="3" width="12" height="9" rx="1" fill="#c7ced3"/><path d="M0 4l6 4 6-4" stroke="#6c7d89" fill="none"/></svg></i><span>sales@velquor.com.au</span></div>
  </div>
  <div class="f-col news" style="left:704px"><h4>NEWSLETER SIGN UP</h4><p>Enter your name and email to subscribe or unsubscribe to receive latest news &amp; offers!!!</p></div>
  <div class="field" style="left:704px;top:135px"><b></b>Enter Your Name</div>
  <div class="field" style="left:704px;top:180px"><b></b>Enter Your Email</div>
  <div class="signup">
    <svg width="28" height="26" viewBox="0 0 28 26"><path d="M27 1L1 12l8 3 2 9 4-6 7 5z" fill="#fff"/></svg>
    SIGN UP
  </div>
</footer>

<div class="abs bottom">
  <div class="copy">© Copyright 2015 Velquor Wireless Internet All Rights Reserved.<b></b><b></b></div>
  <div class="chat"><span>Live Chat Offline</span><span class="sp"></span><i></i><i></i></div>
</div>

</body>
</html>
```